Norvel Hand Wash

Design hand washes. Total 12 variants to be designed.

Variants name are:

1) MILK &OLIVE
2) Shea Butter
3) Hidden Dawn
4) Cream and Peach
5) Milk and Honey
6) Amber Whisper
7) Bakhour
8) Musk
9) White Oud
10) Black Oud
11) Rose Oud
12) Oud & Sandalwood

Labels can be on transparent sticker or background colors. All variants will be differentiated by fragrances and color. Bottle will be transparent. Pumps used for dispensing will be in Black or Transparent Color.

Designers can initially present designs of 4-5 variants initially. Later based on feedback, they can work out on more.

Bottle is 400ml and shape is rectangle. Ignore the size on bottle picture. Bottle keyline is attached.

Target Market(s)

B+, B, C+

Requirements
Must have
• Some relation to the variant names

```html
<!DOCTYPE html>
<html lang="en">
<head>
<meta charset="utf-8">
<title>Norvel Hand Wash – Labels</title>
<link href="https://fonts.googleapis.com/css2?family=Nunito:ital,wght@0,700;0,800;0,900;1,800;1,900&display=swap" rel="stylesheet">
<style>
  :root {
    --bg-center: #ffffff;
    --bg-edge: #dcdcdc;
    --brand-ink: #3b3778;
    --brand-leaf: #6fae2a;
    --white: #ffffff;

    --amber-tint: #f4ebb4;
    --amber-tint-deep: #f0dd93;
    --amber-ribbon: #e59a12;
    --amber-light: #e6a21c;
    --amber-dark: #9c7a2a;
    --amber-art-a: #f3e08a;
    --amber-art-b: #e5b93a;
    --amber-art-c: #6a4a2a;

    --rose-tint: #ef9ec0;
    --rose-tint-deep: #e77fab;
    --rose-ribbon: #c6307a;
    --rose-light: #d65a91;
    --rose-dark: #8e1f5a;
    --rose-art-a: #f3b5c6;
    --rose-art-b: #d65a79;
    --rose-art-c: #a82a4c;

    --peach-tint: #f7c5a3;
    --peach-tint-deep: #f2ab83;
    --peach-ribbon: #e26a26;
    --peach-light: #f08a3c;
    --peach-dark: #9b4b12;
    --peach-art-a: #f6efe6;
    --peach-art-b: #f29b52;
    --peach-art-c: #c3561c;
  }
  * { box-sizing: border-box; margin: 0; padding: 0; }
  html, body { width: 1200px; height: 805px; overflow: hidden; }
  body {
    position: relative;
    background: radial-gradient(ellipse at 50% 40%, var(--bg-center) 45%, var(--bg-edge) 100%);
    font-family: "Nunito", Arial, sans-serif;
  }
  .label {
    position: absolute;
    top: 225px;
    width: 250px;
    height: 380px;
    border-radius: 22px;
    overflow: hidden;
    background: linear-gradient(180deg, var(--tint) 0%, var(--tint-deep) 100%);
    box-shadow: 0 14px 26px rgba(0,0,0,0.12);
  }
  .label--amber { left: 135px; --tint: var(--amber-tint); --tint-deep: var(--amber-tint-deep); --ribbon: var(--amber-ribbon); --light: var(--amber-light); --dark: var(--amber-dark); --art-a: var(--amber-art-a); --art-b: var(--amber-art-b); --art-c: var(--amber-art-c); }
  .label--rose { left: 475px; --tint: var(--rose-tint); --tint-deep: var(--rose-tint-deep); --ribbon: var(--rose-ribbon); --light: var(--rose-light); --dark: var(--rose-dark); --art-a: var(--rose-art-a); --art-b: var(--rose-art-b); --art-c: var(--rose-art-c); }
  .label--peach { left: 815px; --tint: var(--peach-tint); --tint-deep: var(--peach-tint-deep); --ribbon: var(--peach-ribbon); --light: var(--peach-light); --dark: var(--peach-dark); --art-a: var(--peach-art-a); --art-b: var(--peach-art-b); --art-c: var(--peach-art-c); }

  .label__ribbon {
    position: absolute; top: 22px; left: 25px; right: 25px; height: 20px;
    border-radius: 8px 8px 3px 3px;
    background: var(--ribbon);
    color: var(--white);
    font-weight: 900; font-size: 9.5px; letter-spacing: 0.2px;
    display: flex; align-items: center; justify-content: center;
    text-transform: uppercase;
  }
  .label__new {
    position: absolute; top: 50px; left: 30px;
    font-weight: 900; font-size: 14px; color: var(--ribbon);
  }
  .label__brand {
    position: absolute; top: 82px; left: 0; right: 0;
    display: flex; align-items: center; justify-content: center; gap: 8px;
  }
  .label__brand-dot { width: 12px; height: 12px; border-radius: 50%; background: var(--brand-leaf); }
  .label__brand-name { font-weight: 800; font-size: 40px; color: var(--brand-ink); line-height: 1; }
  .label__product {
    position: absolute; top: 138px; left: 0; right: 0; text-align: center;
    font-style: italic; font-weight: 900; font-size: 25px; line-height: 24px;
  }
  .label__product-hand { color: var(--light); display: block; }
  .label__product-wash { color: var(--dark); display: block; }
  .label__art {
    position: absolute; left: 0; right: 0; bottom: 0; height: 160px;
    background: radial-gradient(ellipse at 60% 55%, var(--art-a) 0%, var(--art-b) 55%, var(--art-c) 100%);
    border-top: 2px solid rgba(255,255,255,0.7);
  }
  .label__badge {
    position: absolute; top: 196px; left: 50%; transform: translateX(-50%);
    width: 58px; height: 58px; border-radius: 50%;
    background: var(--ribbon); border: 3px solid var(--white);
    color: var(--white); font-style: italic; font-weight: 900; font-size: 11px; line-height: 11px;
    display: flex; align-items: center; justify-content: center; text-align: center;
    box-shadow: 0 2px 5px rgba(0,0,0,0.2);
  }
  .label__volume {
    position: absolute; bottom: 12px; left: 0; right: 0; text-align: center;
    font-weight: 900; font-size: 15px; color: var(--white);
    text-shadow: 0 1px 2px rgba(0,0,0,0.45);
  }
</style>
</head>
<body>
  <section class="label label--amber">
    <div class="label__ribbon">Kills all known germs!</div>
    <div class="label__new">NEW!</div>
    <div class="label__brand"><span class="label__brand-dot"></span><span class="label__brand-name">Norvel</span></div>
    <div class="label__product"><span class="label__product-hand">Hand</span><span class="label__product-wash">Wash</span></div>
    <div class="label__art" role="img" aria-label="Yellow vanilla orchid flower lying on dark vanilla pods"></div>
    <div class="label__badge">Amber<br>Whisper</div>
    <div class="label__volume">454 mL</div>
  </section>

  <section class="label label--rose">
    <div class="label__ribbon">With natural fragrance!</div>
    <div class="label__new">NEW!</div>
    <div class="label__brand"><span class="label__brand-dot"></span><span class="label__brand-name">Norvel</span></div>
    <div class="label__product"><span class="label__product-hand">Hand</span><span class="label__product-wash">Wash</span></div>
    <div class="label__art" role="img" aria-label="Cluster of pink and red roses"></div>
    <div class="label__badge">Rose<br>Oud</div>
    <div class="label__volume">454 mL</div>
  </section>

  <section class="label label--peach">
    <div class="label__ribbon">With natural fragrance!</div>
    <div class="label__new">NEW!</div>
    <div class="label__brand"><span class="label__brand-dot"></span><span class="label__brand-name">Norvel</span></div>
    <div class="label__product"><span class="label__product-hand">Hand</span><span class="label__product-wash">Wash</span></div>
    <div class="label__art" role="img" aria-label="Ripe peach with a leaf and a splash of cream"></div>
    <div class="label__badge">Cream<br>and<br>Peach</div>
    <div class="label__volume">454 mL</div>
  </section>
</body>
</html>
```